Brightkeel Logistics - Cards and Logo

We need a logo and card design for a Logistics company located in Chicago. Our competitors are KTR and Qorvan. We would like to see designs that incorporate a logo that shows all ways in terms of direction. The colors would be Electric Blue, Grays, Blacks and White. I like how Moko has a badge type logo that is strong and clean. Velmora also has a strong font that is futuristic. The final design should communicate we are a strong and technological type of company. I show a picture of the colors we like from a moko cooler.

```html
<!DOCTYPE html>
<html lang="en">
<head>
<meta charset="utf-8">
<title>Brightkeel Logistics – Business Card</title>
<link href="https://fonts.googleapis.com/css2?family=Josefin+Sans:wght@400&family=Roboto:wght@400;700;900&display=swap" rel="stylesheet">
<style>
  :root {
    --board: #b3b3b3;
    --page: #ffffff;
    --card: #ffffff;
    --band-deep: #1212a0;
    --band-soft: #8a8fd8;
    --brand: #0d129a;
    --name: #2b8fc1;
    --contact: #3a8fc0;
    --icon-1: #0e2a5c;
    --icon-2: #1a4f8a;
    --icon-3: #1b7db2;
    --icon-4: #1aa8e2;
  }
  * { margin: 0; padding: 0; box-sizing: border-box; }
  html, body { width: 1200px; height: 942px; overflow: hidden; background: var(--page); }
  .board {
    position: relative; width: 1200px; height: 942px;
    background: var(--board); border-radius: 48px;
  }
  .card {
    position: absolute; left: 215px; width: 522px; height: 313px;
    background: var(--card); border-radius: 42px; overflow: hidden;
    box-shadow: 0 2px 6px rgba(0,0,0,0.25);
  }
  .card--front { top: 123px; }
  .card--back { top: 490px; }

  .accent-band { position: absolute; left: 0; width: 100%; }
  .accent-band--front {
    bottom: 0; height: 104px;
    background: linear-gradient(to bottom, var(--band-soft), var(--band-deep));
    clip-path: polygon(100% 0, 100% 100%, 0 100%, 0 78%);
  }
  .accent-band--back {
    top: 0; height: 104px;
    background: linear-gradient(to top, var(--band-soft), var(--band-deep));
    clip-path: polygon(0 0, 100% 0, 100% 100%, 0 22%);
  }

  .brand {
    position: absolute; display: flex; align-items: center; gap: 8px;
    font-family: "Roboto", Arial, sans-serif; font-weight: 900;
    color: var(--brand); white-space: nowrap; letter-spacing: -0.2px;
  }
  .brand__mark { background: var(--brand); flex: none; }
  .brand--front { left: 50%; top: 95px; transform: translateX(-50%); font-size: 24px; }
  .brand--front .brand__mark { width: 22px; height: 22px; }
  .brand--back { right: 34px; bottom: 40px; font-size: 14px; gap: 5px; }
  .brand--back .brand__mark { width: 13px; height: 13px; }
  .brand--board { left: 798px; top: 452px; font-size: 24px; }
  .brand--board .brand__mark { width: 22px; height: 22px; }

  .holder { position: absolute; left: 35px; top: 72px; font-family: "Josefin Sans", sans-serif; color: var(--name); }
  .holder__name { font-size: 27px; letter-spacing: 1px; text-transform: uppercase; line-height: 1; }
  .holder__role { font-size: 14px; letter-spacing: 0.8px; text-transform: uppercase; margin-top: 7px; padding-left: 4px; }

  .contacts { position: absolute; left: 36px; top: 166px; list-style: none; font-family: "Roboto", Arial, sans-serif; }
  .contacts li { display: flex; align-items: center; gap: 9px; height: 24px; margin-bottom: 9px; font-size: 15px; color: var(--contact); }
  .contacts .icon { width: 24px; height: 24px; border-radius: 50%; display: flex; align-items: center; justify-content: center; flex: none; }
  .contacts .icon svg { width: 14px; height: 14px; fill: #fff; stroke: #fff; }
  .icon--address { background: var(--icon-1); }
  .icon--web { background: var(--icon-2); }
  .icon--mail { background: var(--icon-3); }
  .icon--phone { background: var(--icon-4); }
</style>
</head>
<body>
<main class="board">

  <section class="card card--front" aria-label="Card front">
    <div class="accent-band accent-band--front" role="img" aria-label="Blue decorative stripe band"></div>
    <div class="brand brand--front"><span class="brand__mark"></span>Brightkeel Logistics</div>
  </section>

  <section class="card card--back" aria-label="Card back">
    <div class="accent-band accent-band--back" role="img" aria-label="Blue decorative stripe band"></div>

    <div class="holder">
      <p class="holder__name">Your Name</p>
      <p class="holder__role">The Position</p>
    </div>

    <ul class="contacts">
      <li><span class="icon icon--address"><svg viewBox="0 0 24 24"><path stroke="none" d="M12 2a7 7 0 0 0-7 7c0 5 7 13 7 13s7-8 7-13a7 7 0 0 0-7-7zm0 9.5A2.5 2.5 0 1 1 12 6.5a2.5 2.5 0 0 1 0 5z"/></svg></span>Your Adress goes here</li>
      <li><span class="icon icon--web"><svg viewBox="0 0 24 24" fill="none"><g fill="none" stroke-width="2"><circle cx="12" cy="12" r="9"/><path d="M3 12h18M12 3c3 3 3 15 0 18M12 3c-3 3-3 15 0 18"/></g></svg></span>website.com</li>
      <li><span class="icon icon--mail"><svg viewBox="0 0 24 24"><rect x="3" y="6" width="18" height="12" stroke="none"/><path d="M3 6l9 7 9-7" fill="none" stroke="#1b7db2" stroke-width="2"/></svg></span>yourweb@email.com</li>
      <li><span class="icon icon--phone"><svg viewBox="0 0 24 24"><path stroke="none" d="M6.6 10.8a15 15 0 0 0 6.6 6.6l2.2-2.2c.3-.3.7-.4 1-.2 1.1.4 2.3.6 3.6.6.6 0 1 .4 1 1V20c0 .6-.4 1-1 1A17 17 0 0 1 3 4c0-.6.4-1 1-1h3.5c.6 0 1 .4 1 1 0 1.3.2 2.5.6 3.6.1.3 0 .7-.2 1z"/></svg></span>123 - 456789</li>
    </ul>

    <div class="brand brand--back"><span class="brand__mark"></span>Brightkeel Logistics</div>
  </section>

  <div class="brand brand--board"><span class="brand__mark"></span>Brightkeel Logistics</div>

</main>
</body>
</html>
```